Open source software project needs static website design

I am looking for a contemporary static web site design and accompanying logo for my open source software project "Quillpath". The project is a library that deals with URLs in web API development and is very cutting edge so this will need to be reflected in the design.

The logo should be modern and striking and derived from the character ʃ (lower case esh). I would like ideally a bold header then a minimal off-white main content area.

The main section on the front page will need to pick out and highlight features of the project using images and larger text, while other pages on the site will primarily feature documentation and code samples.

For inspiration please see: https://varelio.com/, http://dunbrook-mesa.com/, http://pirvo-code.org/

Thanks!

Reason: To give designers a few more days to submit\rework designs based on updated brief

Target Market(s)

Software developers

Industry/Entity Type

Software

Requirements
Must have
• Static web site design provided as HTML\CSS
Nice to have
• Site footer
The content should also feature some mention of http:// and\or API on the front page.

```html
<!DOCTYPE html>
<html lang="en">
<head>
<meta charset="utf-8">
<title>Quillpath – Open Source Web API Development Library</title>
<link rel="stylesheet" href="https://fonts.googleapis.com/css2?family=Oswald:wght@400;500&family=Open+Sans:wght@400;600;700&display=swap">
<style>
:root{
  --teal:#4e7174;
  --teal-dark:#4a6b6e;
  --charcoal:#3a3a3a;
  --orange:#e8930c;
  --panel:#f2f2f2;
  --white:#ffffff;
  --ink:#2b2b2b;
  --muted:#555555;
  --link:#1a7ac0;
  --yellow:#f0c43a;
  --line:#d8d8d8;
}
*{box-sizing:border-box;margin:0;padding:0}
html,body{width:903px;height:1200px;overflow:hidden}
body{position:relative;background:var(--white);font-family:"Open Sans",Arial,sans-serif;color:var(--ink)}
.top-band{position:absolute;left:0;top:0;width:903px;height:289px;background:var(--teal)}
.abs{position:absolute}
.heading{font-family:"Oswald",Arial,sans-serif;font-weight:400;text-transform:uppercase;color:var(--ink)}

/* header */
.brand{left:93px;top:22px;display:flex;align-items:center;gap:8px}
.brand-dot{width:18px;height:18px;border-radius:50%;background:var(--orange)}
.brand-name{font-family:"Oswald",Arial,sans-serif;font-size:26px;font-weight:500;color:var(--orange)}
.brand-sep{left:221px;top:46px;width:1px;height:22px;background:#8aa4a6}
.tagline{left:227px;top:51px;font-family:"Oswald",Arial,sans-serif;font-size:10.5px;color:var(--white);text-transform:uppercase}
.social{left:446px;top:50px;display:flex;font-size:10px;font-weight:700;color:var(--white)}
.social span{display:flex;align-items:center;gap:4px;padding:0 8px;border-right:1px solid #8aa4a6;height:20px}
.social span:last-child{border-right:0}
.social i{width:7px;height:7px;background:var(--white);display:block}
.search-btn{left:668px;top:47px;width:123px;height:24px;background:var(--charcoal);color:var(--white);font-family:"Oswald",Arial,sans-serif;font-size:11px;display:flex;align-items:center;justify-content:center}
.message-bar{left:93px;top:86px;width:698px;height:32px;background:var(--charcoal);border-bottom:3px solid var(--orange);display:flex;justify-content:space-between;align-items:center;padding:0 11px;font-family:"Oswald",Arial,sans-serif;font-size:10px;color:var(--white);text-transform:uppercase}

/* hero */
.hero{left:93px;top:122px;width:697px;height:226px;background:var(--panel)}
.chart-card{left:141px;top:122px;width:298px;height:221px;background:var(--white)}
.chart-title{left:23px;top:10px;font-size:13px;font-weight:600;color:#555}
.legend{left:203px;top:42px;list-style:none;font-size:12.5px;color:#666}
.legend li{display:flex;align-items:center;gap:6px;height:20.5px}
.legend i{width:12px;height:12px;display:block}
.intro{left:485px;top:142px;width:270px}
.intro h1{font-size:15px;margin-bottom:12px}
.intro p{font-size:9px;line-height:12px;color:var(--ink)}
.field{top:267px;width:103px;height:21px;background:var(--white);font-family:"Oswald",Arial,sans-serif;font-size:8px;color:var(--ink);display:flex;align-items:center;justify-content:center;text-transform:uppercase}
.subscribe{left:507px;top:296px;width:216px;height:24px;background:var(--teal);color:var(--white);font-family:"Oswald",Arial,sans-serif;font-size:12.5px;display:flex;align-items:center;justify-content:center;text-transform:uppercase}

/* categories */
.categories-title{left:101px;top:372px;font-size:16px}
.cat{display:flex;align-items:center;gap:12px;font-family:"Oswald",Arial,sans-serif;font-size:12.5px;text-transform:uppercase;color:var(--ink)}
.cat i{display:block;width:28px;height:28px;border-radius:4px}
.view-more{left:679px;top:571px;width:86px;height:20px;display:flex;font-family:"Oswald",Arial,sans-serif;font-size:12px}
.view-more span{flex:1;background:var(--yellow);display:flex;align-items:center;justify-content:center;color:var(--ink)}
.view-more b{width:18px;background:var(--charcoal);display:flex;align-items:center;justify-content:center}
.divider{left:117px;top:630px;width:635px;height:1px;background:var(--line)}

/* editors pick */
.editors-title{left:108px;top:650px;font-size:13px}
.pick{width:182px;height:140px;background:var(--panel);border:1px solid #e3e3e3;padding:18px 14px 0}
.pick h3{font-size:7.5px;font-weight:700;color:var(--ink);padding-bottom:8px;border-bottom:1px solid #e6e6e6}
.pick h3 em{font-style:normal;color:var(--link)}
.pick-body{display:flex;gap:10px;margin-top:22px}
.pick-mark{width:52px;display:flex;align-items:center;gap:3px;font-size:6.5px;font-weight:700;color:#444;flex-shrink:0;padding-top:4px}
.pick-mark i{width:8px;height:8px;background:#3b8cc4;display:block;flex-shrink:0}
.pick-body p{font-size:6.8px;line-height:8.4px;color:#444}

/* footer */
.footer{left:93px;top:994px;width:697px;height:184px;background:var(--panel)}
.footer-col{top:1009px;width:200px}
.footer-col h4{font-family:"Oswald",Arial,sans-serif;font-weight:400;font-size:12px;text-transform:uppercase;margin-bottom:12px}
.footer-col p{font-size:8px;line-height:8.6px;margin-bottom:8px;color:var(--ink)}
.contact-line{font-size:9.5px !important;margin:10px 0 !important}
.bottom-bar{left:0;top:1178px;width:903px;height:22px;background:var(--teal);display:flex;align-items:center;padding-left:101px;gap:6px;font-size:8px;color:#2f4a4c;text-transform:uppercase}
.bottom-bar i{width:9px;height:9px;border:1px solid #2f4a4c;border-radius:50%;display:block}
</style>
</head>
<body>
<div class="top-band"></div>

<header>
  <div class="abs brand"><span class="brand-dot"></span><span class="brand-name">Quillpath</span></div>
  <div class="abs brand-sep"></div>
  <div class="abs tagline">Open Source Web API Development Library</div>
  <nav class="abs social">
    <span><i></i>Chatterly</span>
    <span><i></i>Pinwave</span>
    <span><i></i>Linkfold</span>
  </nav>
  <div class="abs search-btn">SEARCH</div>
  <div class="abs message-bar"><span>Your message here/tage line</span><span>Login / Create Account</span></div>
</header>

<section>
  <div class="abs hero"></div>
  <div class="abs chart-card">
    <div class="abs chart-title">Popular Web API Categories</div>
    <svg class="abs" style="left:16px;top:6px" width="200" height="215" viewBox="0 20 210 215" role="img" aria-label="Pie chart of popular web API categories">
      <g stroke="#fff" stroke-width="1">
        <path d="M105 125 L105 45 A80 80 0 0 1 182.96 107.06Z" fill="#7f9edb"/>
        <path d="M105 125 L182.96 107.06 A80 80 0 0 1 168.51 173.64Z" fill="#e8806a"/>
        <path d="M105 125 L168.51 173.64 A80 80 0 0 1 109.02 204.9Z" fill="#fcbd62"/>
        <path d="M105 125 L109.02 204.9 A80 80 0 0 1 49.87 182.98Z" fill="#6cbd6c"/>
        <path d="M105 125 L49.87 182.98 A80 80 0 0 1 26.33 139.5Z" fill="#bd5fc0"/>
        <path d="M105 125 L26.33 139.5 A80 80 0 0 1 32.4 91.4Z" fill="#5bbcd9"/>
        <path d="M105 125 L32.4 91.4 A80 80 0 0 1 61.72 57.72Z" fill="#e88aa8"/>
        <path d="M105 125 L61.72 57.72 A80 80 0 0 1 105 45Z" fill="#9fc863"/>
      </g>
      <g fill="#fff" font-family="Open Sans, Arial, sans-serif" font-size="11" text-anchor="middle">
        <text x="137" y="90">21.4%</text>
        <text x="157" y="142">14%</text>
        <text x="130" y="182">13.8%</text>
        <text x="80" y="186">12.9%</text>
        <text x="50" y="134">9.8%</text>
      </g>
    </svg>
    <ul class="abs legend">
      <li><i style="background:#7f9edb"></i>Social</li>
      <li><i style="background:#e8806a"></i>Shopping</li>
      <li><i style="background:#fcbd62"></i>Mapping</li>
      <li><i style="background:#6cbd6c"></i>Telephony</li>
      <li><i style="background:#bd5fc0"></i>Music</li>
      <li><i style="background:#5bbcd9"></i>Search</li>
      <li><i style="background:#e88aa8"></i>Photos</li>
      <li><i style="background:#9fc863"></i>Video</li>
    </ul>
  </div>
  <div class="abs intro">
    <h1 class="heading">Open Source Web Development Library</h1>
    <p>Lorem ipsum dolor sit amet, consectetuer adipiscing elit, sed diam nonummy nibh euismod tincidunt ut laoreet dolore magna aliquam erat volutpat. Ut wisi enim ad minim veniam, quis nostrud exerci tation ullamcorper suscipit lobortis nisl ut aliquip ex ea commodo consequat. Duis autem vel eum iriure dolor in hendrerit in vulputate velit esse molestie consequat, vel illum dolore eu feugiat nulla facilisis.</p>
  </div>
  <div class="abs field" style="left:507px">Your name</div>
  <div class="abs field" style="left:620px">Your email address</div>
  <div class="abs subscribe">Subscribe now</div>
</section>

<section>
  <h2 class="abs heading categories-title">Thousands of resources lister in over 100 categories</h2>
  <div class="abs cat" style="left:101px;top:403px"><i role="img" aria-label="Science icon" style="background:#8fb0cf"></i>Science</div>
  <div class="abs cat" style="left:249px;top:403px"><i role="img" aria-label="Photos icon" style="background:#c35ad6"></i>Photos</div>
  <div class="abs cat" style="left:390px;top:403px"><i role="img" aria-label="Science icon" style="background:#8fb0cf"></i>Science</div>
  <div class="abs cat" style="left:538px;top:403px"><i role="img" aria-label="Photos icon" style="background:#c35ad6"></i>Photos</div>
  <div class="abs cat" style="left:687px;top:403px"><i role="img" aria-label="Science icon" style="background:#8fb0cf"></i>Science</div>

  <div class="abs cat" style="left:101px;top:447px"><i role="img" aria-label="Games icon" style="background:#6c7685"></i>Games</div>
  <div class="abs cat" style="left:249px;top:447px"><i role="img" aria-label="Search icon" style="background:#a9c4d8"></i>Search</div>
  <div class="abs cat" style="left:390px;top:447px"><i role="img" aria-label="Games icon" style="background:#6c7685"></i>Games</div>
  <div class="abs cat" style="left:538px;top:447px"><i role="img" aria-label="Search icon" style="background:#a9c4d8"></i>Search</div>
  <div class="abs cat" style="left:687px;top:447px"><i role="img" aria-label="Games icon" style="background:#6c7685"></i>Games</div>

  <div class="abs cat" style="left:101px;top:492px"><i role="img" aria-label="Social icon" style="background:#7d93ad"></i>Social</div>
  <div class="abs cat" style="left:249px;top:492px"><i role="img" aria-label="Shopping icon" style="background:#d2b48a"></i>Shopping</div>
  <div class="abs cat" style="left:390px;top:492px"><i role="img" aria-label="Social icon" style="background:#7d93ad"></i>Social</div>
  <div class="abs cat" style="left:538px;top:492px"><i role="img" aria-label="Shopping icon" style="background:#d2b48a"></i>Shopping</div>
  <div class="abs cat" style="left:687px;top:492px"><i role="img" aria-label="Social icon" style="background:#7d93ad"></i>Social</div>

  <div class="abs cat" style="left:101px;top:535px"><i role="img" aria-label="Internet icon" style="background:#2e4f96"></i>Internet</div>
  <div class="abs cat" style="left:249px;top:535px"><i role="img" aria-label="Video icon" style="background:#555c66"></i>Video</div>
  <div class="abs cat" style="left:390px;top:535px"><i role="img" aria-label="Internet icon" style="background:#2e4f96"></i>Internet</div>
  <div class="abs cat" style="left:538px;top:535px"><i role="img" aria-label="Video icon" style="background:#555c66"></i>Video</div>
  <div class="abs cat" style="left:687px;top:535px"><i role="img" aria-label="Internet icon" style="background:#2e4f96"></i>Internet</div>

  <div class="abs view-more"><span>VIEW MORE</span><b><svg width="10" height="8" viewBox="0 0 10 8"><path d="M1 1l3 3-3 3M5 1l3 3-3 3" stroke="#f0c43a" stroke-width="1.6" fill="none"/></svg></b></div>
  <div class="abs divider"></div>
</section>

<section>
  <h2 class="abs heading editors-title">Editors pick</h2>
  <article class="abs pick" style="left:101px;top:679px">
    <h3><em>FormNest</em> (Business)</h3>
    <div class="pick-body"><div class="pick-mark"><i></i>FormNest</div><p>FormNest API provides simple data retrieval tools for any online forms and surveys you create with the online form builder.</p></div>
  </article>
  <article class="abs pick" style="left:332px;top:678px">
    <h3><em>APIDEX.IO</em> (Other)</h3>
    <div class="pick-body" style="margin-top:24px"><div class="pick-mark"><i></i>APIDEX</div><p>http://apidex.io/</p></div>
  </article>
  <article class="abs pick" style="left:559px;top:679px">
    <h3><em>Seekly</em> (Search)</h3>
    <div class="pick-body" style="margin-top:24px"><div class="pick-mark"><i></i>Seekly</div><p>Seekly Web Search Engine API</p></div>
  </article>

  <article class="abs pick" style="left:101px;top:844px">
    <h3><em>Pipeo</em> (PaaS)</h3>
    <div class="pick-body"><div class="pick-mark"><i></i>Pipeo</div><p>Pipeo is a graph pipelining API talking RESTful JSON, where each node in your graph is responsible for performing a discrete unit of work, su</p></div>
  </article>
  <article class="abs pick" style="left:331px;top:845px">
    <h3><em>CodeCrate</em> (Developer)</h3>
    <div class="pick-body"><div class="pick-mark"><i></i>CodeCrate</div><p>Unlimited DVCS Code Hosting Free up to 5 Users Store all of your distributed version control source code in one place with unlimited private repos. Inc</p></div>
  </article>
  <article class="abs pick" style="left:562px;top:844px">
    <h3><em>TextSense</em> (Social)</h3>
    <div class="pick-body"><div class="pick-mark"><i></i>TextSense</div><p>The purpose of this service is to extract opinions from text. An opinion represents the subject an author is writing about and a sentiment sc</p></div>
  </article>
</section>

<footer>
  <div class="abs footer"></div>
  <div class="abs footer-col" style="left:105px">
    <h4>Contact Information</h4>
    <p>We are more than willing to hear from you. Drop us a line and we will discuss how we can help with your projects.</p>
    <p class="contact-line">QUILLPATH ADDRESS HERE</p>
    <p class="contact-line">Contact Number:</p>
    <p class="contact-line">Email:</p>
  </div>
  <div class="abs footer-col" style="left:346px;width:215px">
    <h4>Latest Tweets</h4>
    <p>Commode Consequat? Sep 13</p>
    <p>Excepteur sint ocaecat cupidat non Proident &nbsp;Sep 13</p>
    <p>Aenean lacinia bibendum nulla sed consetutur_ http://quillpath.com</p>
    <p>Vestibulum id igula porta felis sed euismodspemper.</p>
  </div>
  <div class="abs footer-col" style="left:586px;width:205px">
    <h4 style="padding-left:43px">About Quillpath</h4>
    <p>Commode Consequat? Sep 13</p>
    <p>Excepteur sint ocaecat cupidat non Proident &nbsp;Sep 13</p>
    <p>Aenean lacinia bibendum nulla sed consetutur_ http://quillpath.com</p>
    <p>Vestibulum id igula porta felis sed euismodspemper.</p>
  </div>
  <div class="abs bottom-bar"><i></i>Copyright Quillpath/All rights reserved</div>
</footer>
</body>
</html>
```